National online rug retailer needs a home page design

See the LoomNest logo and create a home page design around that color theme. Details are spelled out in word document uploaded below.
Updates

Apparently this website did not take my attachement showing the logo and basic requirements.  If you would send me your email address, I will send you the attachment directly.
Best regards,
Ned Carver
ncarver@qwplex.com

Target Market(s)

The target market is home owners 25 to 75 years old with combined incomes over $100,000 per year.

Industry/Entity Type

Online

Requirements
Must have
• Lots of white space with black letters and creative use of red and possibly one other color. Would like a compelling call to action button.

```html
<!DOCTYPE html>
<html lang="en">
<head>
<meta charset="utf-8">
<title>LoomNest — Home</title>
<link rel="stylesheet" href="https://fonts.googleapis.com/css2?family=Arimo:wght@400;700&family=Mulish:wght@500;600&family=Open+Sans:wght@400;600&family=Libre+Baskerville:ital@1&display=swap">
<style>
:root{
  --red:#c8101e;
  --ink:#1e1e1e;
  --muted:#777;
  --line:#cfcfcf;
  --bg:#e4e4e4;
  --panel:#ffffff;
  --soft:#ececec;
}
*{box-sizing:border-box;margin:0;padding:0}
html,body{width:1120px;height:1200px;overflow:hidden}
body{background:var(--bg);font-family:"Arimo",Arial,sans-serif;color:var(--ink)}
.stage{position:relative;width:1400px;height:1500px;transform:scale(.8);transform-origin:0 0}
.page{position:absolute;left:209px;top:14px;width:982px;height:1478px;background:var(--panel)}
.abs{position:absolute}
a{color:inherit;text-decoration:none}
.red{color:var(--red)}

/* header */
.logo{left:220px;top:40px;display:flex;align-items:center;gap:10px}
.logo-mark{width:14px;height:14px;background:var(--red)}
.logo-name{font-family:"Open Sans",sans-serif;font-size:38px;font-weight:400;color:#4a4a4a;letter-spacing:-1px;line-height:1}
.tagline{left:309px;top:88px;font-size:12px;color:var(--muted)}
.search{left:558px;top:62px;width:279px;height:36px;border:1px solid var(--line);display:flex;align-items:center;padding:3px}
.search span{flex:1;font-size:12px;color:#444;padding-left:2px}
.search b{background:var(--red);color:#fff;font-weight:400;font-size:16px;height:28px;width:88px;display:flex;align-items:center;justify-content:center;gap:6px}
.cartline{left:902px;top:25px;font-size:12px;color:var(--muted);display:flex;align-items:center;gap:5px}
.cartline strong{color:#666}
.phone{left:902px;top:48px;font-size:14px}
.account{left:903px;top:71px;width:277px;height:27px;display:flex;font-size:12px}
.account > div{background:#dcdcdc;display:flex;align-items:center;padding:0 6px;white-space:nowrap}
.account .chat{flex:1;background:#e4e4e4;margin-left:3px;color:var(--red);gap:8px}
.account .online{color:var(--ink);margin-left:auto}
.nav{left:218px;top:118px;width:963px;height:32px;border:1px solid #e3e3e3;display:flex;align-items:center;padding-left:15px;font-size:12px}
.nav a{padding:0 10px}
.nav a:first-child{padding-left:0;font-weight:700}
.nav i{color:#bbb;font-style:normal}

/* sidebar */
.side{left:220px;top:166px;width:180px}
.browse{font-family:"Mulish",sans-serif;font-size:16px;color:var(--red);font-weight:500;margin-bottom:4px}
.group{border-bottom:1px dashed #bbb;padding:8px 0 8px 2px}
.group h3{font-family:"Mulish",sans-serif;font-weight:500;font-size:15px;display:flex;align-items:center;gap:4px;height:18px}
.dot{width:12px;height:12px;border-radius:50%;background:#777;color:#fff;font-size:11px;line-height:12px;text-align:center;font-family:Arial,sans-serif}
.group ul{list-style:none;padding:6px 0 0 12px;font-size:12px}
.group li{height:30px;line-height:30px}
.group li::before{content:"› ";color:var(--red)}

/* hero */
.hero{left:423px;top:171px;width:758px;height:300px;overflow:hidden;background:linear-gradient(160deg,#d8d4cf 0%,#9b9792 45%,#6f6e6c 100%)}
.hero-title{left:40px;top:84px;font-family:"Open Sans",sans-serif;font-size:42px;color:#111;letter-spacing:.5px}
.hero-box{left:48px;top:130px;width:400px;height:82px;border:1px solid #fff;background:rgba(255,255,255,.45);padding:14px 15px;font-family:"Libre Baskerville",serif;font-style:italic;font-size:19px;line-height:25px;color:#222;white-space:nowrap}
.dots{left:47px;top:271px;display:flex;gap:5px}
.dots span{width:13px;height:13px;border-radius:50%;border:1px solid #fff;background:#bbb}
.burst{left:492px;top:60px}
.ribbon{right:0;bottom:0}

/* features */
.feature{top:491px;width:273px;height:137px;border:1px solid #ddd;padding:5px}
.feature .ph{width:100%;height:126px;position:relative}
.feature .cap{position:absolute;left:0;right:0;bottom:0;height:34px;background:rgba(255,255,255,.7);display:flex;align-items:center;justify-content:space-between;padding:0 8px 0 13px}
.feature .cap b{font-family:"Mulish",sans-serif;font-weight:500;font-size:17px;text-transform:uppercase}
.feature .cap span{font-size:12px;color:var(--red)}

/* product grids */
.sec-title{left:423px;font-family:"Mulish",sans-serif;font-weight:600;font-size:18px;color:var(--red)}
.card{width:177px}
.card .frame{height:127px;border:1px solid #ddd;padding:5px}
.card .ph{width:100%;height:100%}
.card h4{font-family:"Mulish",sans-serif;font-weight:500;font-size:13px;margin-top:7px;text-transform:uppercase;white-space:nowrap}
.card p{font-size:12px;color:var(--red);margin-top:5px}
.rule{left:423px;top:1029px;width:554px;border-top:1px solid #ddd}

/* also-like */
.also{left:994px;top:491px;width:186px;height:537px;background:var(--soft);padding:0 6px 0 12px}
.also h3{font-family:"Mulish",sans-serif;font-weight:600;font-size:16px;color:var(--red);height:52px;line-height:44px}
.mini{display:flex;gap:11px;height:96px;border-bottom:1px dashed #bbb;padding-top:0}
.mini .ph{width:48px;height:72px;flex:none;border:1px solid #fff}
.mini .txt{font-size:12px;line-height:24px;margin-top:-4px;white-space:nowrap}
.mini s{color:#888}
.mini .price{color:var(--red)}
.mini .vd{color:#999}

/* footer */
.foot-rule{left:209px;top:1252px;width:982px;border-top:1px solid #ddd}
.fcol{top:1273px;font-size:12px}
.fcol h5{font-family:"Mulish",sans-serif;font-weight:600;font-size:13px;text-transform:uppercase;margin-bottom:3px}
.fcol ul{list-style:none}
.fcol li{height:18px;line-height:18px}
.fcol li::before{content:"› ";color:var(--red)}
.pay{left:801px;top:1307px;display:flex;gap:6px}
.pay span{width:40px;height:26px;border-radius:3px}
.seals{left:796px;top:1352px;display:flex;gap:10px;align-items:center}
.copy{right:230px;top:1458px;font-size:12px;color:#555}
</style>
</head>
<body>
<div class="stage">
  <div class="page"></div>

  <!-- header -->
  <div class="abs logo"><span class="logo-mark"></span><span class="logo-name">LoomNest.com</span></div>
  <div class="abs tagline">for domestic and heirloom values</div>
  <div class="abs search"><span>enter key words or item #</span><b>Search
    <svg width="14" height="14" viewBox="0 0 14 14"><circle cx="6" cy="6" r="4.5" fill="none" stroke="#fff" stroke-width="2"/><line x1="9.2" y1="9.2" x2="13" y2="13" stroke="#fff" stroke-width="2"/></svg></b></div>
  <div class="abs cartline">
    <svg width="15" height="12" viewBox="0 0 15 12"><path d="M0 1h3l2 7h8l2-5H4" fill="none" stroke="#777" stroke-width="1.6"/><circle cx="6" cy="10.5" r="1.3" fill="#777"/><circle cx="12" cy="10.5" r="1.3" fill="#777"/></svg>
    Items: <span class="red">0</span> | Total: <span class="red">$0.00</span> | <strong>View Cart | Checkout</strong>
  </div>
  <div class="abs phone">Order Toll-Free: 1-888-555-0147</div>
  <div class="abs account">
    <div>My Account | Sign In</div>
    <div class="chat">LIVE CHAT
      <svg width="20" height="14" viewBox="0 0 20 14"><ellipse cx="9" cy="6" rx="8" ry="5.5" fill="#fff"/><path d="M4 10l-1 4 5-3z" fill="#fff"/></svg>
      <span class="online">ONLINE</span></div>
  </div>
  <nav class="abs nav">
    <a>HOME</a><i>|</i><a>SELECTION GUIDES</a><i>|</i><a>RUG CARE</a><i>|</i><a>FAQ</a><i>|</i><a>RETURN POLICY</a><i>|</i><a>FREE SHIPPING</a><i>|</i><a>CLEARANCE RUGS</a>
  </nav>

  <!-- sidebar -->
  <aside class="abs side">
    <div class="browse">BROWSE</div>
    <div class="group" style="padding-top:2px"><h3><span class="dot">−</span>RUG THEME</h3>
      <ul><li>Traditional</li><li>Transitional</li><li>Casual</li></ul></div>
    <div class="group"><h3><span class="dot">−</span>COLOR WAY</h3>
      <ul><li>Black</li><li>Blue</li><li>Green</li><li>Gold</li></ul></div>
    <div class="group"><h3><span class="dot">+</span>SIZE</h3></div>
    <div class="group"><h3><span class="dot">+</span>SHAPE</h3></div>
    <div class="group"><h3><span class="dot">+</span>FIBER CONTENT</h3></div>
    <div class="group"><h3><span class="dot">+</span>MFGR. BRAND</h3></div>
    <div class="group"><h3><span class="dot">+</span>MFGR.COLLECTION</h3></div>
    <div class="group"><h3><span class="dot">+</span>PRICE</h3></div>
  </aside>

  <!-- hero -->
  <section class="abs hero" role="img" aria-label="Living room with a grey patterned rug and navy sofa">
    <div class="abs hero-title">FATHER’S DAY SALE</div>
    <div class="abs hero-box">All rugs. Take an Additional 10% OFF<br>Refer 3 friends and get Another 5% Off</div>
    <div class="abs dots"><span></span><span></span><span></span><span></span><span></span></div>
    <svg class="abs burst" width="180" height="180" viewBox="0 0 180 180">
      <polygon fill="#c8101e" points="90,2 102,20 119,7 125,28 145,20 144,42 166,41 158,61 178,68 164,84 180,98 162,109 172,128 151,131 154,153 133,149 127,171 110,160 97,178 85,161 67,174 62,152 41,158 42,136 20,133 31,114 12,103 28,89 14,72 35,66 27,46 49,46 48,24 69,32 75,11"/>
      <text x="86" y="53" text-anchor="middle" fill="#fff" font-family="Libre Baskerville,serif" font-style="italic" font-size="20">upto</text>
      <text x="64" y="108" text-anchor="middle" fill="#fff" font-family="Libre Baskerville,serif" font-style="italic" font-size="54">50</text>
      <text x="124" y="88" text-anchor="middle" fill="#fff" font-family="Libre Baskerville,serif" font-style="italic" font-size="28">%</text>
      <text x="126" y="120" text-anchor="middle" fill="#fff" font-family="Libre Baskerville,serif" font-style="italic" font-size="30">off</text>
      <text x="72" y="142" text-anchor="middle" fill="#fff" font-family="Arimo,sans-serif" font-weight="700" font-size="12">SHOP NOW ›</text>
    </svg>
    <svg class="abs ribbon" width="112" height="112" viewBox="0 0 112 112">
      <polygon points="112,0 112,112 0,112" fill="#5a5a5a" opacity=".9"/>
      <text x="62" y="80" transform="rotate(-45 62 80)" text-anchor="middle" fill="#ddd" font-family="Open Sans,sans-serif" font-size="16">Ends Monday</text>
    </svg>
  </section>

  <!-- features -->
  <div class="abs feature" style="left:423px"><div class="ph" role="img" aria-label="Modern patchwork rug in brown and cream" style="background:linear-gradient(135deg,#6b5036,#c7b08a 45%,#7a2e22 80%)">
    <div class="cap"><b>Kerman Panel</b><span>$315 - $731</span></div></div></div>
  <div class="abs feature" style="left:706px"><div class="ph" role="img" aria-label="Striped purple and white rug" style="background:linear-gradient(135deg,#9a94a0,#5e58a6 50%,#e9e6f0 75%,#4b4678)">
    <div class="cap"><b>Lorem Ipsum</b><span>$405 - $930</span></div></div></div>

  <!-- also like -->
  <aside class="abs also">
    <h3>YOU MAY ALSO LIKE</h3>
    <div class="mini"><div class="ph" role="img" aria-label="Red patterned rug" style="background:linear-gradient(160deg,#b3202e,#7a0f1c)"></div>
      <div class="txt">Aenean vestibul<br><s>$200</s> <span class="price">$114</span><br><span class="vd">View Details <span class="red">›</span></span></div></div>
    <div class="mini" style="padding-top:2px"><div class="ph" role="img" aria-label="Green rug" style="background:linear-gradient(160deg,#7da24b,#5f8a3a)"></div>
      <div class="txt">Donec interdum<br><s>$300</s> <span class="price">$194</span><br><span class="vd">View Details <span class="red">›</span></span></div></div>
    <div class="mini"><div class="ph" role="img" aria-label="Orange red rug" style="background:linear-gradient(160deg,#d8431f,#b72d17)"></div>
      <div class="txt">&nbsp;Vivamus imperd<br><s>$456</s> <span class="price">$320</span><br><span class="vd">View Details <span class="red">›</span></span></div></div>
    <div class="mini"><div class="ph" role="img" aria-label="Brown and cream striped rug" style="background:linear-gradient(160deg,#5a3a30,#a08878)"></div>
      <div class="txt">Sed placerat<br><s>$350</s> <span class="price">$240</span><br><span class="vd">View Details <span class="red">›</span></span></div></div>
    <div class="mini"><div class="ph" role="img" aria-label="Pink rug" style="background:linear-gradient(160deg,#d86c78,#c44e5c)"></div>
      <div class="txt">Maecenas ac<br><s>$370</s> <span class="price">$280</span><br><span class="vd">View Details <span class="red">›</span></span></div></div>
  </aside>

  <!-- top sellers -->
  <h2 class="abs sec-title" style="top:652px">TOP SELLERS</h2>
  <div class="abs card" style="left:423px;top:676px"><div class="frame"><div class="ph" role="img" aria-label="Cream rug in a living room" style="background:linear-gradient(160deg,#8a7a68,#e4dac8 55%,#6b5a48)"></div></div><h4>Sed quis nisi</h4><p>$230 - $500</p></div>
  <div class="abs card" style="left:612px;top:676px"><div class="frame"><div class="ph" role="img" aria-label="Floral rug with bright petals" style="background:linear-gradient(160deg,#b58a5a,#f0d6c4 40%,#e0609a 70%,#7a5fa8)"></div></div><h4>Fermentum tellus</h4><p>$405 - $930</p></div>
  <div class="abs card" style="left:801px;top:676px"><div class="frame"><div class="ph" role="img" aria-label="Round pink and brown rug" style="background:linear-gradient(160deg,#e2d8d4,#d890a4 50%,#6a3a36)"></div></div><h4>Lobortis quam</h4><p>$455 - $600</p></div>
  <div class="abs card" style="left:423px;top:855px"><div class="frame"><div class="ph" role="img" aria-label="Red shag rug" style="background:linear-gradient(170deg,#3a2a24,#c0201a 50%,#8f1410)"></div></div><h4>Vestibulum condimen</h4><p>$205 - $345</p></div>
  <div class="abs card" style="left:612px;top:855px"><div class="frame"><div class="ph" role="img" aria-label="White shag rug" style="background:linear-gradient(170deg,#cfd6c0,#f1efe6 50%,#dcd8c8)"></div></div><h4>Egestas dignissim</h4><p>$560 - $670</p></div>
  <div class="abs card" style="left:801px;top:855px"><div class="frame"><div class="ph" role="img" aria-label="Black and red swirl pattern rug" style="background:linear-gradient(170deg,#6a6a6a,#efe9dc 45%,#2a2220 75%,#b8261e)"></div></div><h4>Curabitur vel diam</h4><p>$400 - $1000</p></div>
  <div class="abs rule"></div>

  <!-- new arrival -->
  <h2 class="abs sec-title" style="top:1046px">NEW ARRIVAL</h2>
  <div class="abs card" style="left:423px;top:1070px"><div class="frame"><div class="ph" role="img" aria-label="Purple geometric rug" style="background:linear-gradient(150deg,#5a2a7a,#9a3a9a 50%,#6a2a80)"></div></div><h4>Maecenas orci</h4><p>$405</p></div>
  <div class="abs card" style="left:612px;top:1070px"><div class="frame"><div class="ph" role="img" aria-label="Lime green rug in a room" style="background:linear-gradient(170deg,#8a8070,#8bc63a 45%,#6a9a2a)"></div></div><h4>Facilisis feugiat</h4><p>$930</p></div>
  <div class="abs card" style="left:801px;top:1070px"><div class="frame"><div class="ph" role="img" aria-label="Cream rug with brown leaf pattern" style="background:linear-gradient(150deg,#ece3d4,#8a6448 50%,#ece3d4)"></div></div><h4>Semper ut tortor.</h4><p>$430</p></div>

  <!-- footer -->
  <div class="abs foot-rule"></div>
  <div class="abs fcol" style="left:234px"><h5>Customer Service</h5><ul>
    <li>Shipping</li><li>Return Policy</li><li>Privacy Policy</li><li>Ordering &amp; Delivery Checklist</li><li>Terms of Use</li><li>Terms of Sale</li><li>Contact Us</li><li>Environmental Policy</li></ul></div>
  <div class="abs fcol" style="left:437px"><h5>Resources</h5><ul>
    <li>Product Articles</li><li>Learning Center</li><li>Help</li><li>Refer A Friend</li><li>LoomNest Blog</li><li>Room Scene Viewer</li><li>Site Map</li><li>FAQ</li><li>Customer Testimonials</li><li>Photo Gallery</li></ul></div>
  <div class="abs fcol" style="left:618px"><h5>Corporate Info</h5><ul>
    <li>About LoomNest.com</li><li>Careers</li><li>Affiliates</li></ul></div>
  <div class="abs fcol" style="left:799px"><h5 style="font-weight:500">Payment and Security</h5></div>
  <div class="abs pay">
    <span style="background:#2a4a9a"></span><span style="background:#e0602a"></span><span style="background:#e8a040"></span><span style="background:#3a80c0"></span><span style="background:#5a9ad8"></span><span style="background:#9ab0cc"></span>
  </div>
  <div class="abs seals">
    <span style="width:60px;height:54px;border-radius:50%;background:#c8b84a"></span>
    <span style="width:54px;height:54px;border-radius:50%;background:#e6c84a"></span>
    <span style="width:64px;height:26px;border-radius:3px;background:#d8d8d8"></span>
    <span style="width:66px;height:26px;border-radius:3px;background:#1e4a8a"></span>
    <span style="width:78px;height:38px;border-radius:3px;background:#7aa84a"></span>
  </div>
  <div class="abs copy">Copyright © 2013 LoomNest.com. All rights reserved</div>
</div>
</body>
</html>
```